Web-page design

We need a initial web design for our page kelbrook.com.au (which is not yet set up).
We provide consulting services for all kinds of problems in and between organisations.
Main focus is on conflict resolution but we also support companies on improving their operational performance.
We want to have the following page structure (and part of the project is to design the 8 pages):
- Home
- Services (we offer 3 main service areas - one per page)
- Case studies (one per page)
- Engaging us (our process)
- About Conflict & low performance
- Conflict resolution App
- About
- Contact (Email form)
- Our logo should be on each page.
The start page should include the following information:
- Twitter / Linkedin / facebook/ google + Links
- Telephone / Email or in general contact details
- News
- A quite prominent picture box with 3 alternating pics - each representing one of our service areas
- Link to our App
- Testimonials
It would be nice if the service pages would have an image header. Links to the information section (about conflict & low performance; and the app page) would be nice as well.
We like the following joomla designs: www.frandelthemes.com/itempreview/153
No need to copy it, it should just give you an idea.
We like the layout here with the picture and space for the case studies on the left. Somewhere beneath should be the 3 service areas with a picture each.
In terms of colors: our logo colours are Blue (RBG 8;44;80) and Orange (RGB 231;120;23). The orange could be used to emphasise certain things, however there should not be too much color.
Budget for images available, so please use placeholders or ask us for specific photos/images, if you need them for your design.
Updates
Hi, one more thing that we would like to have is the case studies not hidden behind a link "case studies" - we would like to have them individually linked prominent on the first page. There will be about 6-8 of them. Thats what we liked on the joomla template (the links left from the picture).
Hi, thanks very much for all the great proposals.
We are currently going through the selection process and will post our decision early next week.
Thanks again!
Wilma
Target Market(s)
- target customers are all different kinds of businesses and organisations (all industries, government, non-for-profit, ...) experiencing conflict and tension - be it with internal staff, amongst managers or board members, dysfunctional teams, between organizations or customers and organizations... examples could be bullying allegations, governmental negotiations with unions, disputes within organizations etc.
- also we will offer performance improvement services for organizations
- we will offer mediation, facilitation, negotiation, performance improvement services, conflict coaching, conflict management, change management services
- if comparable to anything - then to a law firm in terms of dealing with conflicts but its much less adversarial and much more about the people and their interests rather than about laws
- basically it's all kind of things you can do in order to solve disputes without involving lawyers and a court - so it's much cheaper and target is to find a solution all parties can live with rather than having a judge deciding about who wins and who looses
- performance management is more about analysing reasons for a lack of performance and setting up continous improvement systems, supporting change management, facilitating improvement workshops or strategic meetings, ...
Industry/Entity Type
Consulting
Look and feel

```html
<!DOCTYPE html>
<html lang="en">
<head>
<meta charset="utf-8">
<title>Harlow Brennick – Conflict Resolution &amp; Performance Consulting</title>
<link rel="stylesheet" href="https://fonts.googleapis.com/css2?family=Open+Sans:ital,wght@0,300;0,400;0,600;0,700;1,700&family=Oswald:wght@400&family=PT+Serif:ital,wght@1,700&display=swap">
<style>
:root{
  --navy:#0c2d50;
  --blue:#1d5c98;
  --blue-light:#2f78bd;
  --orange:#e77817;
  --text:#555b61;
  --muted:#8a9096;
  --rule:#dde1e5;
  --panel:#f1f2f4;
  --nav:#3a3e44;
  --nav-dark:#2b2e33;
  --footer:#2d2f32;
  --footer-deep:#222427;
  --white:#ffffff;
}
*{box-sizing:border-box;margin:0;padding:0}
html,body{width:720px;height:1200px;overflow:hidden}
body{font-family:"Open Sans",Arial,sans-serif;color:var(--text);background:var(--white);font-size:8px;line-height:1.45}
.wrap{width:544px;margin:0 auto;position:relative}
a{color:inherit;text-decoration:none}

/* top bar */
.topbar{height:19px;background:var(--navy);color:#cfd9e4;font-size:7px}
.topbar .wrap{display:flex;justify-content:space-between;align-items:center;height:19px}
.topbar .contact span{margin-right:16px}
.topbar .links span{margin-left:10px}

/* header */
.header{height:72px}
.header .wrap{display:flex;justify-content:space-between;align-items:center;height:72px}
.brand-name{font-weight:600;font-size:20px;color:var(--navy);letter-spacing:.2px;line-height:1.2}
.brand-url{font-size:7.5px;color:var(--muted);letter-spacing:1.6px;margin-top:3px}
.app-link{text-align:right}
.app-link .label{font-size:7.5px;font-weight:700;color:var(--navy);letter-spacing:.4px;margin-bottom:6px}
.social{display:flex;gap:5px;justify-content:flex-end}
.social span{width:18px;height:18px;border-radius:50%;background:var(--blue)}

/* nav */
.nav{height:26px;background:linear-gradient(var(--nav),var(--nav-dark))}
.nav ul{list-style:none;display:flex;height:26px;align-items:center}
.nav li{display:flex;align-items:center;gap:5px;color:#e3e6ea;font-size:7.5px;padding:0 11px;height:26px;border-right:1px solid #4a4f56}
.nav li.active{background:var(--orange);color:var(--white)}
.nav svg{width:9px;height:9px}

/* hero */
.hero{height:240px;position:relative;background:linear-gradient(160deg,#7aa4c4 0%,#456f93 45%,#1f3c58 100%)}
.hero-photo{position:absolute;inset:0}
.hero-caption{position:absolute;left:144px;top:160px;width:372px;height:34px;background:rgba(12,45,80,.82);color:var(--white);font-family:"Oswald",sans-serif;font-size:20px;display:flex;align-items:center;padding-left:12px;border-left:4px solid var(--orange)}

/* features */
.features{background:var(--panel);height:156px;border-bottom:1px solid var(--rule)}
.features .wrap{display:flex;gap:10px;padding-top:18px}
.feature{flex:1;font-size:6.5px;color:var(--muted)}
.feature.intro{padding-top:2px}
.feature-head{display:flex;gap:6px;align-items:center;margin-bottom:8px}
.feature-icon{width:20px;height:20px;border-radius:50%;background:var(--navy);flex:none;display:flex;align-items:center;justify-content:center}
.feature-title{font-size:7px;font-weight:700;color:var(--navy);line-height:1.2;text-transform:uppercase}
.more{color:var(--blue-light);font-weight:600;display:block;margin-top:5px}

/* services */
.services{padding-top:26px;height:240px}
.section-head{display:flex;justify-content:space-between;align-items:center;border-bottom:1px solid var(--rule);padding-bottom:6px;margin-bottom:12px}
.section-title{font-weight:300;font-size:17px;color:var(--navy)}
.btn-dark{background:var(--nav-dark);color:var(--white);font-size:6.5px;padding:3px 7px}
.cards{display:flex;gap:32px}
.card{flex:1;text-align:center;border-bottom:3px solid var(--orange)}
.card-photo{height:118px}
.card-photo.one{background:linear-gradient(180deg,#7fb5e0,#3a78a8 70%,#2b5d86)}
.card-photo.two{background:linear-gradient(180deg,#9fc9e8,#c9a66a 60%,#7c6a42)}
.card-photo.three{background:linear-gradient(180deg,#bfd8ec,#e2c48f 55%,#9b7f52)}
.card-body{background:var(--panel);padding:5px 0 6px}
.card-title{font-size:13px;color:var(--blue);line-height:1.2}
.card-sub{font-size:7px;color:var(--text)}

/* lower */
.lower{display:flex;gap:26px;height:232px;padding-top:10px}
.tabbox{width:288px;height:190px;border:1px solid var(--rule)}
.tabs{display:flex;border-bottom:1px solid var(--rule)}
.tab{font-size:6.5px;font-weight:700;padding:6px 14px;color:var(--muted);background:var(--panel);border-right:1px solid var(--rule)}
.tab.active{background:var(--white);color:var(--navy)}
.tab-body{display:flex;gap:12px;padding:14px}
.tab-text{width:120px;font-size:7px;color:var(--text)}
.tab-photo{width:126px;height:90px;margin-top:10px;background:linear-gradient(150deg,#dbe6ee,#8fb0c8 60%,#5a7d98)}
.btn-orange{display:inline-block;background:var(--orange);color:var(--white);font-size:7px;font-weight:600;padding:4px 10px;margin-top:10px;border-radius:2px}
.news{flex:1}
.news .section-title{margin-bottom:4px}
.news-item{display:flex;gap:8px;padding:8px 0;border-bottom:1px solid var(--rule)}
.news-photo{width:64px;height:50px;flex:none;position:relative;background:linear-gradient(150deg,#c7dbea,#6d96b8)}
.news-date{position:absolute;left:0;top:4px;background:var(--orange);color:var(--white);font-size:6.5px;font-weight:700;padding:1px 4px}
.news-title{font-size:8px;color:var(--orange);line-height:1.25}
.news-text{font-size:6.5px;color:var(--muted);margin-top:2px}

/* newsletter */
.band{height:36px;background:var(--blue)}
.band .wrap{display:flex;align-items:center;height:36px;color:var(--white)}
.band .call{font-family:"PT Serif",serif;font-style:italic;font-weight:700;font-size:11px;width:170px}
.band .subscribe{font-family:"PT Serif",serif;font-style:italic;font-weight:700;font-size:12px;flex:1}
.band .form{display:flex}
.band .field{width:104px;height:14px;background:var(--white);color:var(--muted);font-size:6px;padding:2px 5px}
.band .submit{height:14px;background:var(--nav-dark);font-size:6px;padding:3px 6px}

/* footer */
.footer{height:155px;background:var(--footer);color:#b9bec4;position:relative}
.footer .wrap{display:flex;gap:20px;padding-top:16px}
.col{flex:1;font-size:7px}
.col.wide{flex:1.4}
.col h4{font-family:"PT Serif",serif;font-style:italic;font-weight:700;font-size:8.5px;color:var(--white);text-transform:uppercase;margin-bottom:8px;letter-spacing:.3px}
.col ul{list-style:none}
.col li{line-height:1.7}
.contact-row{display:flex;line-height:1.7}
.contact-row b{width:40px;font-weight:600;color:var(--white)}
.quote{background:#3a3d41;padding:8px;font-style:italic;font-size:7px}
.quote .by{text-align:right;margin-top:4px;color:var(--orange);font-style:normal}
.to-top{position:absolute;right:20px;bottom:10px;width:22px;height:22px;background:#111;display:flex;align-items:center;justify-content:center}
.copy{height:24px;background:var(--footer-deep);color:#8d9298;font-size:6.5px}
.copy .wrap{height:24px;display:flex;align-items:center;justify-content:center}
</style>
</head>
<body>

<div class="topbar">
  <div class="wrap">
    <div class="contact"><span>✉ info@kelbrook.com.au</span><span>✆ +61 3 9000 4172</span></div>
    <div class="links"><span>Login</span><span>|</span><span>Privacy</span><span>|</span><span>Site map</span></div>
  </div>
</div>

<header class="header">
  <div class="wrap">
    <div class="brand">
      <div class="brand-name">Harlow Brennick</div>
      <div class="brand-url">www.kelbrook.com.au</div>
    </div>
    <div class="app-link">
      <div class="label">LOGIN TO OUR APP</div>
      <div class="social" aria-label="Social links"><span></span><span></span><span></span><span></span></div>
    </div>
  </div>
</header>

<nav class="nav">
  <div class="wrap">
    <ul>
      <li class="active"><svg viewBox="0 0 10 10"><path d="M1 5 5 1l4 4H8v4H2V5z" fill="#fff"/></svg>Home</li>
      <li><svg viewBox="0 0 10 10"><circle cx="5" cy="3" r="2" fill="#fff"/><path d="M1 10a4 4 0 0 1 8 0z" fill="#fff"/></svg>About Us</li>
      <li><svg viewBox="0 0 10 10"><circle cx="5" cy="5" r="3.5" fill="none" stroke="#fff" stroke-width="1.6"/></svg>Services</li>
      <li><svg viewBox="0 0 10 10"><path d="M1 1h8v6H4L2 9V7H1z" fill="#fff"/></svg>Testimonials</li>
      <li><svg viewBox="0 0 10 10"><rect x="1" y="3" width="8" height="6" fill="#fff"/><rect x="3.5" y="1" width="3" height="2" fill="none" stroke="#fff"/></svg>Careers</li>
      <li><svg viewBox="0 0 10 10"><circle cx="5" cy="5" r="4" fill="#fff"/></svg>Support</li>
      <li><svg viewBox="0 0 10 10"><path d="M1 9l1-3 5-5 2 2-5 5z" fill="#fff"/></svg>Blog</li>
      <li><svg viewBox="0 0 10 10"><rect x="1" y="2" width="8" height="6" fill="#fff"/></svg>Contact</li>
    </ul>
  </div>
</nav>

<section class="hero">
  <div class="hero-photo" role="img" aria-label="Photo of business people in suits holding black umbrellas under a cloudy sky"></div>
  <div class="hero-caption">This is Photoshop's version &nbsp;of Lorem</div>
</section>

<section class="features">
  <div class="wrap">
    <div class="feature intro">Lorem ipsum dolor sit amet, consectetur adipiscing elit. Morbi tempor purus quis augue egestas, vitae pretium nisi facilisis. Donec at nibh ac lorem pulvinar.<a class="more">Read more</a></div>
    <div class="feature">
      <div class="feature-head"><span class="feature-icon"><svg width="10" height="10" viewBox="0 0 10 10"><circle cx="5" cy="5" r="3" fill="none" stroke="#fff" stroke-width="1.4"/></svg></span><span class="feature-title">Business<br>Technologies</span></div>
      Lorem ipsum dolor sit amet, consectetur elit. Integer vitae nisi et ipsum facilisis finibus.<a class="more">Read More</a>
    </div>
    <div class="feature">
      <div class="feature-head"><span class="feature-icon"><svg width="10" height="10" viewBox="0 0 10 10"><rect x="2" y="2" width="6" height="6" fill="#fff"/></svg></span><span class="feature-title">Management</span></div>
      Lorem ipsum dolor sit amet, consectetur adipiscing elit. Morbi euismod placerat leo et tincidunt.<a class="more">Read More</a>
    </div>
    <div class="feature">
      <div class="feature-head"><span class="feature-icon"><svg width="10" height="10" viewBox="0 0 10 10"><path d="M1 9h8M2 8V5M5 8V2M8 8V4" stroke="#fff" stroke-width="1.4"/></svg></span><span class="feature-title">Sales Analysis</span></div>
      Phasellus lobortis rutrum erat, quis aliquet dolor. Vestibulum commodo felis at magna sodales.<a class="more">Read More</a>
    </div>
    <div class="feature">
      <div class="feature-head"><span class="feature-icon"><svg width="10" height="10" viewBox="0 0 10 10"><circle cx="4" cy="4" r="2.5" fill="none" stroke="#fff" stroke-width="1.4"/><path d="M6 6l3 3" stroke="#fff" stroke-width="1.4"/></svg></span><span class="feature-title">Market<br>Research</span></div>
      Vivamus sed lacus pellentesque, tempus nulla ut, blandit lorem. Nunc aliquam dolor non mattis.<a class="more">Read More</a>
    </div>
  </div>
</section>

<section class="services">
  <div class="wrap">
    <div class="section-head"><h2 class="section-title">Our Services</h2><span class="btn-dark">View All</span></div>
    <div class="cards">
      <div class="card"><div class="card-photo one" role="img" aria-label="Photo of a city skyline under a blue sky"></div><div class="card-body"><div class="card-title">Lorem ipsum</div><div class="card-sub">Management</div></div></div>
      <div class="card"><div class="card-photo two" role="img" aria-label="Photo of a collection of famous world landmarks"></div><div class="card-body"><div class="card-title">Lorem ipsum</div><div class="card-sub">Management</div></div></div>
      <div class="card"><div class="card-photo three" role="img" aria-label="Photo of a landmark building at sunset"></div><div class="card-body"><div class="card-title">Lorem ipsum</div><div class="card-sub">Business</div></div></div>
    </div>
  </div>
</section>

<section class="wrap lower">
  <div class="tabbox">
    <div class="tabs"><span class="tab active">ABOUT US</span><span class="tab">LATEST WORK</span></div>
    <div class="tab-body">
      <div class="tab-text">This is Photoshop's version of Lorem Ipsum. Proin gravida nibh vel velit auctor aliquet. Aenean sollicitudin, lorem quis bibendum auctor, nisi elit consequat ipsum, nec sagittis sem nibh id elit. Duis sed odio sit amet nibh vulputate cursus a sit amet mauris.<br><span class="btn-orange">Read More</span></div>
      <div class="tab-photo" role="img" aria-label="Photo of a consultant working at a laptop in a bright office"></div>
    </div>
  </div>
  <div class="news">
    <h2 class="section-title">Latest News</h2>
    <div class="news-item">
      <div class="news-photo" role="img" aria-label="Photo of a business meeting"><span class="news-date">25 Jan</span></div>
      <div><div class="news-title">This is Photoshop's version of Lorem Ipsum. Pro</div><div class="news-text">Nibh vel velit auctor aliquet aenean sollicitudin lorem quis bibendum auctor nisi elit.</div></div>
    </div>
    <div class="news-item">
      <div class="news-photo" role="img" aria-label="Photo of colleagues discussing plans"><span class="news-date">25 Jan</span></div>
      <div><div class="news-title">This is Photoshop's version of Lorem Ipsum. Pro</div><div class="news-text">Nibh vel velit auctor aliquet aenean sollicitudin lorem quis bibendum auctor nisi elit.</div></div>
    </div>
  </div>
</section>

<section class="band">
  <div class="wrap">
    <div class="call">Call us! +1 300 555 018</div>
    <div class="subscribe">Subscribe to Our Newsletter</div>
    <div class="form"><span class="field">email address here</span><span class="submit">SUBMIT</span></div>
  </div>
</section>

<footer class="footer">
  <div class="wrap">
    <div class="col"><h4>Information</h4><ul><li>About us</li><li>Our works</li><li>Terms of Service</li><li>Privacy Policy</li><li>Comment Agreement</li><li>Contact Us</li></ul></div>
    <div class="col"><h4>Our Services</h4><ul><li>Management Plan</li><li>Business Plans</li><li>Sales Analysis</li><li>Management</li></ul></div>
    <div class="col wide"><h4>Get in Touch</h4>
      <div class="contact-row"><b>Address:</b><span>14/8 Carrow Lane Road,<br>Northvale VIC 3000</span></div>
      <div class="contact-row"><b>Phone:</b><span>+1 300 555 018</span></div>
      <div class="contact-row"><b>Fax:</b><span>+1 300 555 019</span></div>
      <div class="contact-row"><b>Email:</b><span>info@kelbrook.com.au</span></div>
    </div>
    <div class="col wide"><h4>Testimonials</h4><div class="quote">"Lorem ipsum dolor sit amet, consectetur adipiscing elit. Sed non risus suspendisse lectus tortor dignissim sit amet adipiscing nec."<div class="by">By Lorem Ipsum</div></div></div>
  </div>
  <span class="to-top"><svg width="10" height="8" viewBox="0 0 10 8"><path d="M1 7l4-5 4 5" fill="none" stroke="#fff" stroke-width="1.8"/></svg></span>
</footer>
<div class="copy"><div class="wrap">© 2013 kelbrook.com.au · All rights reserved</div></div>

</body>
</html>
```